Relationship Seminar

I am an Author and Speaker and I need a flyer for a Christian relationship seminar targeting women aged between mid 20's to late 30's. It's an event for women only.

-I am looking for a fresh/ edgy look but still feminine
-Nothing too girly
-Maximum of 3 colours (Spring colours are good)
-I want the flyer to convey joy or happiness
-Use my photo which is attached as the predominant image (you can crop it to remove the background etc)

The Flyer Details are as follows:

Somewhere Along The Way - Brisbane Tour

Join Author & Speaker, Rosalind Kupferle, as she speaks about her new book entitled 'Somewhere Along The Way'.

Be inspired and encouraged to embrace the life that God has given you and make the most of it!

Date: Saturday 9th November 2013
Time: 2:00 pm - 5:00 pm
Location: Harwick Lodge Brisbane (Juniper Hall)
Pelham Crescent, Brisbane QLD 4000
Tickets: $60/pp (Includes High Tea)
Buy Tickets: www.rosalindkupferle.com or http://somewherealongtheway.ticketquarry.net

Email: info@rosalindkupferle.com

Include the cover of my new book.

www.rosalindkupferle.com (include my website at the bottom of the flyer)

Target Market(s)

Young professional women aged between their mid 20's to late 30's

Industry/Entity Type

Event

Requirements
Should not have
• -No girly or curly font

```html
<!DOCTYPE html>
<html lang="en">
<head>
<meta charset="utf-8">
<title>Somewhere Along The Way – Brisbane Tour</title>
<link href="https://fonts.googleapis.com/css2?family=Cinzel:wght@600;700&family=Open+Sans:wght@600;700&display=swap" rel="stylesheet">
<style>
  :root {
    --orange: #f26b12;
    --green: #8cc63f;
    --green-soft: #b6da6a;
    --ink: #1e1e1e;
    --paper: #ffffff;
    --backdrop: #f7f8ee;
    --photo-light: #e8ddd6;
    --photo-mid: #c9a99a;
    --photo-dark: #3a2a26;
    --cover-light: #eeeeee;
    --cover-mid: #c9c9cc;
  }
  * { box-sizing: border-box; margin: 0; padding: 0; }
  html, body {
    width: 1200px; height: 848px; overflow: hidden;
    background: var(--backdrop);
  }
  .flyer {
    position: absolute; left: 228px; top: 160px;
    width: 762px; height: 508px;
    background: var(--paper);
    font-family: "Open Sans", Arial, sans-serif;
    color: var(--ink);
    overflow: hidden;
  }
  .event-title {
    position: absolute; left: 0; top: 18px; width: 380px;
    text-align: center;
    font-family: "Cinzel", Georgia, serif;
    font-weight: 700;
    color: var(--orange);
    line-height: 1.05;
  }
  .event-title .line-main { display: block; font-size: 44px; }
  .event-title .line-sub { display: block; font-size: 36px; margin-top: 6px; }
  .tour-name {
    position: absolute; left: 0; top: 126px; width: 380px;
    text-align: center;
    font-family: "Cinzel", Georgia, serif;
    font-weight: 600; font-size: 24px;
    color: var(--green);
  }
  .speaker-photo {
    position: absolute; left: 369px; top: 0; width: 393px; height: 168px;
    background: linear-gradient(90deg, var(--paper) 0%, var(--photo-light) 25%, var(--photo-mid) 60%, var(--photo-dark) 85%, var(--photo-mid) 100%);
  }
  .book-cover {
    position: absolute; left: 78px; top: 184px; width: 146px; height: 272px;
    background: linear-gradient(180deg, var(--cover-light) 0%, var(--cover-mid) 100%);
    border-bottom: 8px solid var(--green);
    box-shadow: -6px 6px 10px rgba(0,0,0,0.18);
  }
  .intro {
    position: absolute; left: 288px; top: 180px; width: 454px;
    font-size: 14.5px; font-weight: 700; line-height: 1.5;
    text-align: justify; text-indent: 32px;
  }
  .intro .speaker-name {
    font-family: "Cinzel", Georgia, serif;
    color: var(--orange); font-size: 16px;
  }
  .details {
    position: absolute; left: 288px; top: 277px; width: 454px;
    list-style: none;
  }
  .details li {
    display: flex; height: 20px; margin-bottom: 3px;
    font-size: 12.5px; font-weight: 700; line-height: 20px;
  }
  .details .label {
    width: 106px; margin-right: 2px;
    background: var(--orange); color: var(--paper);
    font-size: 14px; padding-left: 4px;
    border-radius: 4px 0 0 4px;
  }
  .details .label.empty { background: transparent; }
  .details .value {
    flex: 1; background: var(--green-soft);
    padding-left: 18px; border-radius: 0 4px 4px 0;
  }
  .site-band {
    position: absolute; left: 0; bottom: 0; width: 762px; height: 40px;
    background: var(--orange); color: var(--paper);
    text-align: center;
    font-family: "Cinzel", Georgia, serif;
    font-weight: 700; font-size: 28px; line-height: 40px;
    letter-spacing: 1px;
  }
</style>
</head>
<body>
  <main class="flyer">
    <h1 class="event-title">
      <span class="line-main">Somewhere</span>
      <span class="line-sub">Along The Way</span>
    </h1>
    <p class="tour-name">Brisbane Tour</p>

    <div class="speaker-photo" role="img" aria-label="Smiling portrait of author Rosalind Kupferle against a whitewashed brick wall"></div>

    <div class="book-cover" role="img" aria-label="Cover of the book 'Somewhere Along The Way' by Rosalind Kupferle"></div>

    <p class="intro">Join Author &amp; Speaker, <span class="speaker-name">Rosalind Kupferle</span>, as she speaks about her new book entitled 'Somewhere Along The Way'. Be inspired and encouraged to embrace the life that God has given you and make the most of it!</p>

    <ul class="details">
      <li><span class="label">DATE</span><span class="value">Saturday 9th November 2013</span></li>
      <li><span class="label">TIME</span><span class="value">2:00 pm - 5:00 pm</span></li>
      <li><span class="label">LOCATION</span><span class="value">Harwick Lodge Brisbane (Juniper Hall)</span></li>
      <li><span class="label empty"></span><span class="value">Pelham Crescent, Brisbane QLD 4000</span></li>
      <li><span class="label">TICKETS</span><span class="value">$60/pp (Includes High Tea)</span></li>
      <li><span class="label">BUY TICKETS</span><span class="value">www.rosalindkupferle.com</span></li>
      <li><span class="label empty"></span><span class="value">http://somewherealongtheway.ticketquarry.net</span></li>
      <li><span class="label">EMAIL</span><span class="value">info@rosalindkupferle.com</span></li>
    </ul>

    <footer class="site-band">WWW.ROSALINDKUPFERLE.COM</footer>
  </main>
</body>
</html>
```